Heronby Mortgage Capital Business Card

We need a business card design for our mortgage servicing company. In addition to servicing the loans of homeowners, we help homeowners with purchasing their homes and any mortgage refinancing. We would like to see designs that use the colors in the logo attached below (gold-ish yellow and navy blue), and any other design you deem fit! The design should communicate a simpler life with smart mortgages provided by Heronby.

```html
<!DOCTYPE html>
<html lang="en">
<head>
<meta charset="utf-8">
<title>Heronby Mortgage Capital – Business Card</title>
<link href="https://fonts.googleapis.com/css2?family=Lato:wght@400;700&family=Montserrat:wght@600;700&display=swap" rel="stylesheet">
<style>
  :root {
    --navy: #2c2760;
    --navy-deep: #231f52;
    --gold: #e3b23c;
    --paper: #ffffff;
    --ink: #2c2760;
    --stage: #1c1c1e;
  }
  * { margin: 0; padding: 0; box-sizing: border-box; }
  html, body { width: 1200px; height: 900px; overflow: hidden; }
  body { background: var(--stage); position: relative; font-family: 'Lato', sans-serif; }

  .card {
    position: absolute;
    width: 600px;
    height: 343px;
    overflow: hidden;
  }

  /* Front */
  .card--front {
    left: 90px; top: 80px;
    background: linear-gradient(135deg, var(--navy) 0%, var(--navy-deep) 100%);
    display: flex; align-items: center; justify-content: center;
  }
  .brand {
    display: flex; align-items: center; gap: 14px;
    font-family: 'Montserrat', sans-serif;
    font-weight: 700;
    color: var(--gold);
  }
  .brand__dot { width: 18px; height: 18px; border-radius: 50%; background: var(--gold); flex: none; }
  .card--front .brand__name { font-size: 46px; letter-spacing: 0.5px; }

  /* Back */
  .card--back { left: 510px; top: 470px; background: var(--paper); }
  .card--back .brand { position: absolute; left: 48px; top: 48px; }
  .card--back .brand__name { font-size: 30px; }
  .card--back .brand__dot { width: 13px; height: 13px; }

  .accent-bar { position: absolute; width: 12px; }
  .accent-bar--gold { left: 62px; bottom: 0; height: 110px; background: var(--gold); }
  .accent-bar--navy { right: 0; top: 58px; height: 90px; background: var(--navy); }

  .holder {
    position: absolute; right: 48px; top: 110px; text-align: right;
    font-family: 'Montserrat', sans-serif;
  }
  .holder__name { font-size: 25px; font-weight: 700; color: var(--ink); letter-spacing: 0.3px; }
  .holder__role { font-size: 15px; font-weight: 600; color: var(--gold); margin-top: 2px; }

  .contact-list {
    position: absolute; left: 100px; top: 150px;
    list-style: none; color: var(--ink); font-size: 14px; line-height: 1.3;
  }
  .contact-list li { display: flex; align-items: flex-start; gap: 10px; margin-bottom: 5px; }
  .contact-list svg { width: 13px; height: 13px; flex: none; margin-top: 2px; fill: var(--ink); }
</style>
</head>
<body>

  <section class="card card--front" aria-label="Card front">
    <div class="brand">
      <span class="brand__dot"></span>
      <span class="brand__name">Heronby Mortgage</span>
    </div>
  </section>

  <section class="card card--back" aria-label="Card back">
    <div class="brand">
      <span class="brand__dot"></span>
      <span class="brand__name">Heronby Mortgage</span>
    </div>

    <div class="holder">
      <div class="holder__name">DANIEL REYES</div>
      <div class="holder__role">Founder &amp; CEO</div>
    </div>

    <ul class="contact-list">
      <li>
        <svg viewBox="0 0 24 24"><path d="M12 2a7 7 0 0 0-7 7c0 5 7 13 7 13s7-8 7-13a7 7 0 0 0-7-7zm0 9.5A2.5 2.5 0 1 1 12 6.5a2.5 2.5 0 0 1 0 5z"/></svg>
        <span>Your Address, Your City<br>State, Zip Code 1235</span>
      </li>
      <li>
        <svg viewBox="0 0 24 24"><path d="M6.6 10.8a15 15 0 0 0 6.6 6.6l2.2-2.2a1 1 0 0 1 1-.25 11.4 11.4 0 0 0 3.6.57 1 1 0 0 1 1 1V20a1 1 0 0 1-1 1A17 17 0 0 1 3 4a1 1 0 0 1 1-1h3.5a1 1 0 0 1 1 1c0 1.25.2 2.45.57 3.6a1 1 0 0 1-.25 1z"/></svg>
        <span>(123) 456-7890</span>
      </li>
      <li>
        <svg viewBox="0 0 24 24"><path d="M7 1h10a2 2 0 0 1 2 2v18a2 2 0 0 1-2 2H7a2 2 0 0 1-2-2V3a2 2 0 0 1 2-2zm0 3v14h10V4zm5 15.5a1 1 0 1 0 0 2 1 1 0 0 0 0-2z"/></svg>
        <span>(231) 456-7890</span>
      </li>
      <li>
        <svg viewBox="0 0 24 24"><path d="M6 2h12v5H6zM4 8h16a2 2 0 0 1 2 2v7h-4v5H6v-5H2v-7a2 2 0 0 1 2-2zm4 8v4h8v-4z"/></svg>
        <span>(312) 456-7890</span>
      </li>
      <li>
        <svg viewBox="0 0 24 24"><path d="M2 5h20v14H2zm2 2v.5l8 5 8-5V7z"/></svg>
        <span>hello@heronbymortgage.com</span>
      </li>
      <li>
        <svg viewBox="0 0 24 24"><path d="M12 2a10 10 0 1 0 0 20 10 10 0 0 0 0-20zm6.9 9h-3a15 15 0 0 0-1.3-5.5A8 8 0 0 1 18.9 11zM12 4.1A13 13 0 0 1 13.9 11h-3.8A13 13 0 0 1 12 4.1zM9.4 5.5A15 15 0 0 0 8.1 11h-3a8 8 0 0 1 4.3-5.5zM5.1 13h3a15 15 0 0 0 1.3 5.5A8 8 0 0 1 5.1 13zm6.9 6.9a13 13 0 0 1-1.9-6.9h3.8a13 13 0 0 1-1.9 6.9zm2.6-1.4a15 15 0 0 0 1.3-5.5h3a8 8 0 0 1-4.3 5.5z"/></svg>
        <span>www.heronbymortgage.com</span>
      </li>
    </ul>

    <div class="accent-bar accent-bar--gold"></div>
    <div class="accent-bar accent-bar--navy"></div>
  </section>

</body>
</html>
```